we need a business card. We are an online company that provides work life balance services to our members. our website can be viewed at www.merrow4tide.com.au
Our company logo is attached as well as a business card look that i like.

```html
<!DOCTYPE html>
<html lang="en">
<head>
<meta charset="utf-8">
<title>merrow4tide business card</title>
<link rel="stylesheet" href="https://fonts.googleapis.com/css2?family=Abel&family=Open+Sans:ital,wght@0,400;1,400&display=swap">
<style>
  :root {
    --page: #ffffff;
    --card-edge: #c6e3c6;
    --ink: #111111;
    --muted: #9a9a9a;
    --lime: #8cc63f;
    --leaf: #2e8b2e;
    --forest-deep: #1e3a02;
    --forest-mid: #0b4a05;
    --forest-bright: #237f02;
    --pale: #d4d4d4;
  }
  html, body {
    margin: 0;
    padding: 0;
    width: 1031px;
    height: 1200px;
    overflow: hidden;
    background: var(--page);
  }
  .sheet {
    position: relative;
    width: 1031px;
    height: 1200px;
  }
  .card {
    position: absolute;
    left: 58px;
    width: 912px;
    height: 529px;
    border: 2px solid var(--card-edge);
    border-radius: 2px;
    overflow: hidden;
  }
  .card--front { top: 58px; background: var(--page); }
  .card--back  { top: 607px; background: var(--forest-deep); }

  .front-brand {
    position: absolute;
    left: 150px;
    top: 246px;
    display: flex;
    align-items: center;
    gap: 10px;
    font-family: "Open Sans", sans-serif;
    font-size: 30px;
    color: var(--leaf);
  }
  .front-brand__dot {
    width: 14px;
    height: 14px;
    border-radius: 50%;
    background: var(--lime);
  }

  .contact {
    position: absolute;
    left: 484px;
    top: 137px;
    font-family: "Abel", sans-serif;
    color: var(--ink);
  }
  .contact__name {
    margin: 0;
    font-size: 46px;
    font-weight: 400;
    letter-spacing: 0.5px;
    line-height: 1;
  }
  .contact__role {
    margin: 10px 0 0;
    font-size: 19px;
    color: var(--muted);
  }
  .contact__list {
    list-style: none;
    margin: 22px 0 0;
    padding: 0;
    font-size: 25px;
  }
  .contact__row { display: flex; line-height: 36px; }
  .contact__row--gap { margin-bottom: 8px; }
  .contact__key {
    width: 27px;
    color: var(--lime);
    font-weight: 700;
  }
  .contact__key--inline { margin-left: 18px; }
  .contact__address { line-height: 36px; }

  .back-pattern {
    position: absolute;
    inset: 0;
    background:
      radial-gradient(ellipse 30% 45% at 88% 60%, var(--forest-bright), transparent 70%),
      radial-gradient(ellipse 22% 18% at 30% 5%, var(--forest-bright), transparent 70%),
      radial-gradient(ellipse 30% 20% at 80% 8%, var(--forest-mid), transparent 70%),
      radial-gradient(ellipse 18% 45% at 10% 50%, var(--forest-mid), transparent 70%),
      radial-gradient(ellipse 30% 12% at 30% 98%, var(--forest-bright), transparent 70%),
      var(--forest-deep);
  }
  .back-brand {
    position: absolute;
    left: 245px;
    top: 226px;
    font-family: "Open Sans", sans-serif;
  }
  .back-brand__name {
    margin: 0;
    font-size: 70px;
    line-height: 1;
    color: var(--pale);
    letter-spacing: -1px;
  }
  .back-brand__tagline {
    margin: 6px 0 0 2px;
    font-size: 19px;
    font-style: italic;
    color: var(--pale);
  }
</style>
</head>
<body>
<div class="sheet">
  <section class="card card--front">
    <div class="front-brand">
      <span class="front-brand__dot"></span>
      <span>merrow4tide</span>
    </div>
    <div class="contact">
      <h1 class="contact__name">Nolan Brevik</h1>
      <p class="contact__role">Owner / Manager</p>
      <ul class="contact__list">
        <li class="contact__row contact__row--gap"><span class="contact__key">P</span>02 9417 3350<span class="contact__key contact__key--inline">F</span>02 8765 0412</li>
        <li class="contact__row"><span class="contact__key">E</span>info@merrow4tide.com.au</li>
        <li class="contact__row contact__row--gap"><span class="contact__key">W</span>www.merrow4tide.com.au</li>
        <li class="contact__row"><span class="contact__key">A</span><span class="contact__address">First Floor, 42 Harbour View Road<br>Wollara Point, NSW 2061</span></li>
      </ul>
    </div>
  </section>

  <section class="card card--back">
    <div class="back-pattern" role="img" aria-label="Large decorative brand symbol in layered greens across the card back"></div>
    <div class="back-brand">
      <p class="back-brand__name">merrow4tide</p>
      <p class="back-brand__tagline">steady tides - thriving ventures</p>
    </div>
  </section>
</div>
</body>
</html>
```